Kestrow Fire Services Pty Ltd

We need business cards for a company based in Perth, we install, service and maintain fire equipment.
On the front we want a great design with our logo and a small spot for our full company name, general company email address and office number. On the back we need space for our name, title, mobile number and email address on the back.

Target Market(s)

Facility managers and commercial/industrial building owners/occupiers.

Contact Information for Business Card

Font styles to use
Sans Serif

Requirements
Must have
• Please only submit 5 of your best samples.
Darker tones are preferred.
Nice to have
• We want to use, black, red and grey. Keep it modern and clean.
I've attached the company logo and a sample of a boarder we use on our emergency plans.
Should not have
• No preference. Let the designer choose.

```html
<!DOCTYPE html>
<html lang="en">
<head>
<meta charset="utf-8">
<title>Kestrow Fire Services – Business Cards</title>
<link rel="stylesheet" href="https://fonts.googleapis.com/css2?family=Montserrat:wght@700&family=Roboto:wght@300;400;900&display=swap">
<style>
  :root {
    --stage: #2b2b2d;
    --stage-light: #4a4a4d;
    --card-grey: #3b3b3d;
    --card-grey-deep: #2e2e30;
    --card-black: #111112;
    --red: #ee1c25;
    --white: #f2f2f2;
    --muted: #1f1f21;
  }
  * { box-sizing: border-box; margin: 0; padding: 0; }
  html, body { width: 1200px; height: 1200px; overflow: hidden; }
  body {
    background: radial-gradient(ellipse at 50% 35%, var(--stage-light), var(--stage) 75%);
    font-family: "Roboto", sans-serif;
    position: relative;
  }
  .card {
    position: absolute;
    left: 190px;
    width: 820px;
    height: 470px;
    border-radius: 28px;
    overflow: hidden;
  }
  /* Company side */
  .card--company { top: 95px; background: var(--card-grey); }
  .company-mark {
    position: absolute;
    top: 140px; left: 0; width: 100%;
    text-align: center;
    font-family: "Roboto", sans-serif;
    font-weight: 900;
    font-size: 96px;
    letter-spacing: 4px;
    color: var(--card-grey-deep);
  }
  .company-details {
    position: absolute;
    bottom: 48px; left: 0; width: 100%;
    text-align: center;
    color: var(--muted);
    font-weight: 400;
    font-size: 18px;
    letter-spacing: 0.5px;
    line-height: 1.5;
  }
  .company-details .dot {
    display: inline-block;
    width: 7px; height: 7px;
    border-radius: 50%;
    background: var(--red);
    vertical-align: middle;
    margin: 0 8px;
  }
  /* Personal side */
  .card--personal { top: 630px; background: var(--card-black); }
  .brand-name {
    position: absolute;
    top: 70px; right: 60px;
    font-family: "Roboto", sans-serif;
    font-weight: 900;
    font-size: 78px;
    letter-spacing: 2px;
    color: var(--red);
  }
  .person {
    position: absolute;
    top: 205px; left: 60px;
  }
  .person-name {
    font-family: "Montserrat", sans-serif;
    font-weight: 700;
    font-size: 30px;
    letter-spacing: 5px;
    color: var(--red);
  }
  .person-title {
    margin-top: 4px;
    font-weight: 400;
    font-size: 17px;
    letter-spacing: 4px;
    color: var(--white);
  }
  .divider {
    position: absolute;
    top: 292px; left: 180px;
    width: 580px; height: 2px;
    background: var(--red);
  }
  .contact-list {
    position: absolute;
    top: 318px; left: 440px;
    list-style: none;
  }
  .contact-list li {
    display: flex;
    align-items: center;
    gap: 16px;
    font-weight: 400;
    font-size: 22px;
    letter-spacing: 2px;
    color: var(--white);
    height: 38px;
  }
  .contact-list svg { width: 18px; height: 18px; flex: none; }
</style>
</head>
<body>
  <section class="card card--company">
    <div class="company-mark">KESTROW</div>
    <div class="company-details">
      <p><span class="dot"></span>Your FullCompanyName<span class="dot"></span></p>
      <p>123 456 7890 | youremail.com</p>
    </div>
  </section>

  <section class="card card--personal">
    <div class="brand-name">KESTROW</div>
    <div class="person">
      <p class="person-name">MARCUS HALE</p>
      <p class="person-title">FOUNDER &amp; CEO</p>
    </div>
    <div class="divider"></div>
    <ul class="contact-list">
      <li>
        <svg viewBox="0 0 24 24" aria-hidden="true"><path fill="#ee1c25" d="M6.6 10.8a15 15 0 0 0 6.6 6.6l2.2-2.2c.3-.3.7-.4 1-.2 1.1.4 2.3.6 3.6.6.6 0 1 .4 1 1V20c0 .6-.4 1-1 1A17 17 0 0 1 3 4c0-.6.4-1 1-1h3.5c.6 0 1 .4 1 1 0 1.3.2 2.5.6 3.6.1.3 0 .7-.2 1z"/></svg>
        +61 412 387 905
      </li>
      <li>
        <svg viewBox="0 0 24 24" aria-hidden="true"><rect x="2" y="5" width="20" height="14" rx="1.5" fill="#ee1c25"/><path d="M3 6l9 7 9-7" fill="none" stroke="#111112" stroke-width="1.6"/></svg>
        ceo@kestrowfire.com
      </li>
      <li>
        <svg viewBox="0 0 24 24" aria-hidden="true"><g fill="none" stroke="#ee1c25" stroke-width="1.8"><circle cx="12" cy="12" r="9.5"/><ellipse cx="12" cy="12" rx="4" ry="9.5"/><path d="M2.5 12h19M4 7h16M4 17h16"/></g></svg>
        www.kestrowfire.com
      </li>
    </ul>
  </section>
</body>
</html>
```